Copper Lantern Fitness Flyer

We need a Flyer designed for a Revolutionary Fresh New Functional Fitness facility in Manly Sydney, Australia. We have just recently opened and now need to get the word out. Using the flyers to hand out at events also for shop counters and letterbox drops.

Our company name is Copper Lantern Fitness "Where STRENGTH Becomes Your SPARK".
We promote health and fitness to all fitness levels concentrating on functional fitness. To learn more about us and our colour scheme see attached file and also check us out on www.brightvine-social.example/copperlanternfitnessgroup

A5 Size please

Target Market(s)

The beauty of our system is it is for everyone we have girls and guys in there teens, 20's 30's 40's and 50's. Not only that we have professional athletes, military and high fitness levels all the way to people who are overweight and need to loose weight and tone up. The system caters for everyone.

Industry/Entity Type

Fitness

Requirements
Must have
• FRONT:

Free 30min Fat Blasting Experience With Your Very Own Personal Trainer !!!

New Class Starts Every 3 minutes.
30 minute Workout With A Trainer.
No Machines No Mirrors And No Attitudes.
Catering For All Fitness Levels.
Results Guaranteed Or Your Money Back.
Fun, Fresh, Clean, Revolutionary New Facility.

Back:

You Are Just Moments Away From Burning Fat Faster Than Ever Before And Getting That Body You Always Wanted !!!

Come In Today To Claim Your FREE Workout.

Ph (02) 9417 2086
Address 5/127 Greywattle Ave Fernbrook 2178
www.brightvine-social.example/copperlanternfitnessgroup
Nice to have
• FRONT:

Back:

Ph (02) 9417 2086

```html
<!DOCTYPE html>
<html lang="en">
<head>
<meta charset="utf-8">
<title>Copper Lantern Fitness Flyer</title>
<link rel="stylesheet" href="https://fonts.googleapis.com/css2?family=Roboto+Condensed:ital,wght@0,700;1,300;1,400;1,700&display=swap">
<style>
  :root {
    --canvas: #ffffff;
    --panel: #2f3331;
    --yellow: #f5e500;
    --red: #e0201b;
    --green: #4fd400;
    --orange: #f08a1c;
    --title-yellow: #ffe400;
    --copy: #e6e6e6;
    --white: #ffffff;
    --logo-ink: #2b3a66;
  }
  * { margin: 0; padding: 0; box-sizing: border-box; }
  html, body { width: 1200px; height: 1000px; overflow: hidden; background: var(--canvas); }
  body { position: relative; font-family: "Roboto Condensed", "Arial Narrow", sans-serif; }

  .flyer {
    position: absolute; top: 115px; width: 516px; height: 732px;
    background: var(--panel); overflow: hidden;
    box-shadow: 0 6px 14px rgba(0,0,0,0.12);
  }
  .flyer--front { left: 47px; }
  .flyer--back { left: 620px; }

  .layer { position: absolute; left: 0; top: 0; width: 516px; height: 732px; }
  .hero-photo { position: absolute; left: 0; top: 0; width: 516px; height: 340px; }
  .oval-photo { position: absolute; }

  .headline {
    position: absolute; left: 32px; top: 312px;
    font-weight: 700; font-style: italic; font-size: 31px; line-height: 32px;
    color: var(--title-yellow); letter-spacing: 0.2px;
  }
  .headline em { font-style: italic; color: var(--orange); }

  .offer {
    position: absolute; left: 34px; top: 380px;
    font-weight: 700; font-style: italic; font-size: 12.5px; line-height: 16px; color: var(--white);
  }

  .benefits { position: absolute; left: 30px; top: 442px; list-style: none; }
  .benefit { position: relative; height: 52px; padding-left: 50px; }
  .benefit__num {
    position: absolute; left: 0; top: 2px; width: 34px; height: 32px; border-radius: 50%;
    background: var(--orange); border: 2px solid var(--white);
    color: var(--white); font-weight: 700; font-style: italic; font-size: 18px;
    display: flex; align-items: center; justify-content: center;
  }
  .benefit__text {
    font-style: italic; font-weight: 400; font-size: 12.5px; line-height: 15px; color: var(--copy);
  }

  .pitch {
    position: absolute; left: 32px; top: 396px;
    font-style: italic; font-weight: 300; font-size: 15.5px; line-height: 21px; color: var(--copy);
  }
  .claim {
    position: absolute; left: 32px; top: 474px;
    font-style: italic; font-weight: 300; font-size: 15.5px; line-height: 20px; color: var(--copy);
  }
  .claim strong { font-weight: 700; color: var(--white); }
  .contact {
    position: absolute; left: 32px; top: 530px;
    font-style: italic; font-weight: 300; font-size: 12px; line-height: 16px; color: var(--copy);
  }

  .brand {
    position: absolute; left: 31px; top: 656px; width: 106px; height: 56px;
    background: var(--white); border-radius: 7px;
    display: flex; align-items: center; gap: 6px; padding: 0 7px;
  }
  .brand__mark { width: 18px; height: 18px; background: var(--orange); flex: none; }
  .brand__name {
    font-weight: 700; font-size: 11px; line-height: 11px; color: var(--logo-ink); text-transform: uppercase;
  }
</style>
</head>
<body>

<!-- FRONT -->
<section class="flyer flyer--front">
  <svg class="hero-photo" viewBox="0 0 516 340" role="img" aria-label="Photo: two women doing a plank exercise in a bright studio">
    <defs>
      <linearGradient id="heroFront" x1="0" y1="0" x2="1" y2="1">
        <stop offset="0" stop-color="#e9e2c8"/>
        <stop offset="0.45" stop-color="#c99a74"/>
        <stop offset="1" stop-color="#8a6a55"/>
      </linearGradient>
    </defs>
    <path d="M0 0 H516 V304 Q260 272 0 236 Z" fill="url(#heroFront)"/>
  </svg>

  <svg class="layer" viewBox="0 0 516 732" aria-hidden="true">
    <path d="M0 232 Q260 266 516 298 L516 306 Q260 276 0 240 Z" fill="var(--yellow)"/>
    <path d="M0 240 Q260 276 516 306 L516 330 Q260 292 0 248 Z" fill="var(--red)"/>
    <path d="M0 594 Q300 600 516 672 L516 690 Q300 628 0 622 Z" fill="var(--yellow)"/>
    <path d="M0 624 Q300 630 516 692 L516 702 Q300 650 0 650 Z" fill="var(--green)"/>
    <ellipse cx="412" cy="308" rx="66" ry="60" fill="var(--green)"/>
    <ellipse cx="414" cy="312" rx="64" ry="58" fill="var(--yellow)"/>
    <ellipse cx="414" cy="484" rx="78" ry="70" fill="var(--yellow)"/>
    <ellipse cx="426" cy="635" rx="70" ry="66" fill="var(--red)"/>
    <ellipse cx="424" cy="639" rx="69" ry="65" fill="var(--yellow)"/>
  </svg>

  <svg class="oval-photo" style="left:342px;top:255px" width="130" height="122" viewBox="0 0 130 122" role="img" aria-label="Photo: trainer coaching a woman on a treadmill">
    <defs><linearGradient id="fo1" x1="0" y1="0" x2="1" y2="1"><stop offset="0" stop-color="#e8e6e2"/><stop offset="1" stop-color="#7a6e68"/></linearGradient></defs>
    <ellipse cx="65" cy="61" rx="61" ry="57" fill="url(#fo1)" stroke="var(--white)" stroke-width="5"/>
  </svg>
  <svg class="oval-photo" style="left:343px;top:408px" width="154" height="140" viewBox="0 0 154 140" role="img" aria-label="Photo: smiling couple working out on exercise bikes">
    <defs><linearGradient id="fo2" x1="0" y1="0" x2="1" y2="1"><stop offset="0" stop-color="#d9d2cc"/><stop offset="1" stop-color="#6d6460"/></linearGradient></defs>
    <ellipse cx="77" cy="70" rx="73" ry="66" fill="url(#fo2)" stroke="var(--white)" stroke-width="5"/>
  </svg>
  <svg class="oval-photo" style="left:353px;top:578px" width="136" height="130" viewBox="0 0 136 130" role="img" aria-label="Photo: group fitness class in a gym">
    <defs><linearGradient id="fo3" x1="0" y1="0" x2="1" y2="1"><stop offset="0" stop-color="#cfc8c0"/><stop offset="1" stop-color="#5e5856"/></linearGradient></defs>
    <ellipse cx="68" cy="65" rx="64" ry="61" fill="url(#fo3)" stroke="var(--white)" stroke-width="5"/>
  </svg>

  <h1 class="headline">Where <em>STRENGTH</em><br>Becomes Your <em>SPARK</em></h1>
  <p class="offer">Free 30min Fat Blasting Experience<br>With Your Very Own Personal Trainer !!!</p>

  <ul class="benefits">
    <li class="benefit"><span class="benefit__num">1</span><p class="benefit__text">New Class Starts Every 3 minutes.<br>30 minute Workout With A Trainer.</p></li>
    <li class="benefit"><span class="benefit__num">2</span><p class="benefit__text">No Machines No Mirrors And No Attitudes.<br>Catering For All Fitness Levels.</p></li>
    <li class="benefit"><span class="benefit__num">3</span><p class="benefit__text">Results Guaranteed Or Your Money Back.<br>Fun, Fresh, Clean, Revolutionary New Facility.</p></li>
  </ul>

  <div class="brand"><span class="brand__mark"></span><span class="brand__name">Copper<br>Lantern<br>Fitness</span></div>
</section>

<!-- BACK -->
<section class="flyer flyer--back">
  <svg class="hero-photo" viewBox="0 0 516 340" role="img" aria-label="Photo: functional training gym floor with sprint track, turf and bikes">
    <defs>
      <linearGradient id="heroBack" x1="0" y1="0" x2="1" y2="1">
        <stop offset="0" stop-color="#d8d8d6"/>
        <stop offset="0.4" stop-color="#6e6a66"/>
        <stop offset="0.7" stop-color="#3b3b3a"/>
        <stop offset="1" stop-color="#4f8a3a"/>
      </linearGradient>
    </defs>
    <path d="M0 0 H516 V304 Q260 272 0 236 Z" fill="url(#heroBack)"/>
  </svg>

  <svg class="layer" viewBox="0 0 516 732" aria-hidden="true">
    <path d="M0 232 Q260 266 516 298 L516 306 Q260 276 0 240 Z" fill="var(--yellow)"/>
    <path d="M0 240 Q260 276 516 306 L516 330 Q260 292 0 248 Z" fill="var(--red)"/>
    <path d="M0 594 Q300 600 516 672 L516 690 Q300 628 0 622 Z" fill="var(--yellow)"/>
    <path d="M0 624 Q300 630 516 692 L516 702 Q300 650 0 650 Z" fill="var(--green)"/>
    <ellipse cx="424" cy="300" rx="66" ry="62" fill="var(--green)"/>
    <ellipse cx="422" cy="304" rx="64" ry="60" fill="var(--yellow)"/>
    <ellipse cx="394" cy="478" rx="68" ry="66" fill="var(--yellow)"/>
    <ellipse cx="424" cy="642" rx="70" ry="66" fill="var(--red)"/>
    <ellipse cx="422" cy="646" rx="69" ry="65" fill="var(--yellow)"/>
  </svg>

  <svg class="oval-photo" style="left:352px;top:242px" width="134" height="126" viewBox="0 0 134 126" role="img" aria-label="Photo: man lifting with a trainer spotting">
    <defs><linearGradient id="bo1" x1="0" y1="0" x2="1" y2="1"><stop offset="0" stop-color="#e4e2e0"/><stop offset="1" stop-color="#6a605c"/></linearGradient></defs>
    <ellipse cx="67" cy="63" rx="63" ry="59" fill="url(#bo1)" stroke="var(--white)" stroke-width="5"/>
  </svg>
  <svg class="oval-photo" style="left:334px;top:408px" width="130" height="130" viewBox="0 0 130 130" role="img" aria-label="Photo: woman training with dumbbells on a bench">
    <defs><linearGradient id="bo2" x1="0" y1="0" x2="1" y2="1"><stop offset="0" stop-color="#d6d2cc"/><stop offset="1" stop-color="#55504c"/></linearGradient></defs>
    <ellipse cx="65" cy="65" rx="61" ry="61" fill="url(#bo2)" stroke="var(--white)" stroke-width="5"/>
  </svg>
  <svg class="oval-photo" style="left:344px;top:583px" width="148" height="136" viewBox="0 0 148 136" role="img" aria-label="Photo: personal trainer guiding a woman through a workout">
    <defs><linearGradient id="bo3" x1="0" y1="0" x2="1" y2="1"><stop offset="0" stop-color="#e2ddd6"/><stop offset="1" stop-color="#7a6a62"/></linearGradient></defs>
    <ellipse cx="74" cy="68" rx="70" ry="64" fill="url(#bo3)" stroke="var(--white)" stroke-width="5"/>
  </svg>

  <h2 class="headline">Where <em>STRENGTH</em><br>Becomes Your <em>SPARK</em></h2>
  <p class="pitch">You Are Just Moments Away From<br>Burning Fat Faster Than Ever Before And<br>Getting That Body You Always Wanted !!!</p>
  <p class="claim">Come In Today To Claim Your<br><strong>FREE Workout.</strong></p>
  <p class="contact">Ph (02) 9417 2086<br>Address 5/127 Greywattle Ave Fernbrook 2178<br>www.brightvine-social.example/copperlanternfitnessgroup</p>

  <div class="brand"><span class="brand__mark"></span><span class="brand__name">Copper<br>Lantern<br>Fitness</span></div>
</section>

</body>
</html>
```